Autodetailing namecard design: Rose Gold Lettering on Black Matt

This is a namecard design project
requiring two-sided design
Base Color of Namecard: black matt

On front:
Company name,
"Lumina Finishes 14 Cendana"
Subtext: Auto Detailing Studio

Name of card holder: Marcus Oyelaran
Phone Number: +6011-4837-5062
address: 14, Jalan Cendana 5/3Taman Seri Cendana, 81400 Johor Bahru, Johor, Malaysia

Back:
Our Services
High Gloss Car Paint Protection
Custom Color Modification and Styling
Anti-Chip Glass Protection Film
Heat Rejection Glass Tinting

Target Market(s)

Autodetailing for highend cars

Contact Information for Business Card

as mentioned in project details

Colors

Designer to choose colors to be used in the design.

Requirements
Must have
• The main value-add to this project is the design of a logo suited for our purpose and name, and the inclusion of business card details into the card design

```html
<!DOCTYPE html>
<html lang="en">
<head>
<meta charset="utf-8">
<title>Lumina Finishes 14 Cendana – Business Card</title>
<link href="https://fonts.googleapis.com/css2?family=Montserrat:wght@300;400;500;700;800&display=swap" rel="stylesheet">
<style>
  :root {
    --backdrop: #ececec;
    --matt-black: #1c1c1c;
    --matt-black-deep: #121212;
    --car-tone: #2c2c2c;
    --rose-gold: #d2a08c;
    --rose-gold-deep: #b7796a;
    --text-light: #f4f1ef;
    --text-soft: #c9c4c1;
  }
  * { margin: 0; padding: 0; box-sizing: border-box; }
  html, body { width: 1200px; height: 796px; overflow: hidden; }
  body {
    background: var(--backdrop);
    font-family: "Montserrat", sans-serif;
    display: flex;
    align-items: center;
    justify-content: center;
    gap: 60px;
  }
  .card {
    width: 530px;
    height: 304px;
    position: relative;
    overflow: hidden;
    background: linear-gradient(180deg, var(--matt-black) 0%, var(--matt-black-deep) 100%);
    color: var(--text-light);
    box-shadow: 0 10px 28px rgba(0,0,0,0.2);
  }
  .car-visual {
    position: absolute;
    background: radial-gradient(ellipse at 50% 50%, var(--car-tone) 0%, rgba(28,28,28,0) 70%);
  }

  .brand-lockup {
    display: flex;
    align-items: center;
    justify-content: center;
    gap: 8px;
  }
  .brand-dot {
    width: 10px; height: 10px;
    border-radius: 50%;
    background: var(--rose-gold);
    flex: none;
  }
  .brand-name {
    font-weight: 800;
    font-size: 17px;
    letter-spacing: 0.4px;
    text-transform: uppercase;
    color: var(--text-light);
  }
  .brand-tagline {
    color: var(--rose-gold);
    font-weight: 400;
    font-size: 11px;
    letter-spacing: 1px;
    text-transform: uppercase;
    margin-top: 3px;
  }

  /* Back side */
  .card--back { text-align: center; }
  .card--back .car-visual { left: 70px; top: 70px; width: 390px; height: 180px; border-radius: 90px 120px 30px 30px; }
  .back-content { position: relative; padding-top: 50px; }
  .rule-accent {
    width: 300px; height: 2px;
    background: var(--rose-gold);
    margin: 12px auto 18px;
  }
  .services-title {
    font-weight: 800;
    font-size: 17px;
    text-transform: uppercase;
    margin-bottom: 10px;
  }
  .services-list { list-style: none; }
  .services-list li {
    color: var(--rose-gold);
    font-size: 12px;
    font-weight: 500;
    text-transform: uppercase;
    letter-spacing: 0.6px;
    line-height: 20px;
    display: flex;
    align-items: center;
    justify-content: center;
    gap: 8px;
  }
  .chevron { width: 10px; height: 8px; flex: none; }

  /* Front side */
  .card--front .car-visual { left: 40px; top: 26px; width: 450px; height: 142px; border-radius: 80px 130px 10px 10px; }
  .front-hero {
    position: absolute; left: 0; top: 0;
    width: 100%; height: 168px;
  }
  .front-hero .brand-block {
    position: absolute;
    left: 0; right: 0; top: 64px;
    text-align: center;
  }
  .front-hero .brand-name { font-size: 20px; }
  .front-hero .brand-tagline { font-size: 13px; }
  .front-band-rule {
    position: absolute;
    left: 40px; right: 40px; top: 168px;
    height: 1px;
    background: rgba(210,160,140,0.35);
  }
  .holder {
    position: absolute;
    left: 34px; top: 215px;
    font-size: 20px;
    text-transform: uppercase;
    letter-spacing: 0.5px;
  }
  .holder-first { font-weight: 800; color: var(--text-light); }
  .holder-last { font-weight: 300; color: var(--rose-gold); }
  .divider {
    position: absolute;
    left: 290px; top: 188px;
    width: 2px; height: 86px;
    background: var(--rose-gold);
  }
  .contact {
    position: absolute;
    left: 310px; top: 192px;
    color: var(--text-soft);
    font-size: 11px;
    line-height: 15px;
    font-style: normal;
  }
  .contact-phone { margin-top: 10px; font-size: 13px; font-weight: 500; color: var(--text-light); }
</style>
</head>
<body>

  <section class="card card--back" aria-label="Card back">
    <div class="car-visual" role="img" aria-label="Dark photo of a sports hatchback in shadow"></div>
    <div class="back-content">
      <div class="brand-lockup">
        <span class="brand-dot"></span>
        <h2 class="brand-name">Lumina Finishes 14 Cendana</h2>
      </div>
      <p class="brand-tagline">Auto Detailing Studio</p>
      <div class="rule-accent"></div>
      <h3 class="services-title">Our Services</h3>
      <ul class="services-list">
        <li><svg class="chevron" viewBox="0 0 10 8"><path d="M1 1l3 3-3 3M5 1l3 3-3 3" fill="none" stroke="#f4f1ef" stroke-width="1.3"/></svg>High Gloss Car Paint Protection<svg class="chevron" viewBox="0 0 10 8"><path d="M9 1L6 4l3 3M5 1L2 4l3 3" fill="none" stroke="#f4f1ef" stroke-width="1.3"/></svg></li>
        <li><svg class="chevron" viewBox="0 0 10 8"><path d="M1 1l3 3-3 3M5 1l3 3-3 3" fill="none" stroke="#f4f1ef" stroke-width="1.3"/></svg>Custom Color Modification and Styling<svg class="chevron" viewBox="0 0 10 8"><path d="M9 1L6 4l3 3M5 1L2 4l3 3" fill="none" stroke="#f4f1ef" stroke-width="1.3"/></svg></li>
        <li><svg class="chevron" viewBox="0 0 10 8"><path d="M1 1l3 3-3 3M5 1l3 3-3 3" fill="none" stroke="#f4f1ef" stroke-width="1.3"/></svg>Anti-Chip Glass Protection Film<svg class="chevron" viewBox="0 0 10 8"><path d="M9 1L6 4l3 3M5 1L2 4l3 3" fill="none" stroke="#f4f1ef" stroke-width="1.3"/></svg></li>
        <li><svg class="chevron" viewBox="0 0 10 8"><path d="M1 1l3 3-3 3M5 1l3 3-3 3" fill="none" stroke="#f4f1ef" stroke-width="1.3"/></svg>Heat Rejection Glass Tinting<svg class="chevron" viewBox="0 0 10 8"><path d="M9 1L6 4l3 3M5 1L2 4l3 3" fill="none" stroke="#f4f1ef" stroke-width="1.3"/></svg></li>
      </ul>
    </div>
  </section>

  <section class="card card--front" aria-label="Card front">
    <div class="front-hero">
      <div class="car-visual" role="img" aria-label="Dark side-view photo of a sports hatchback"></div>
      <div class="brand-block">
        <div class="brand-lockup">
          <span class="brand-dot"></span>
          <h1 class="brand-name">Lumina Finishes 14 Cendana</h1>
        </div>
        <p class="brand-tagline">Auto Detailing Studio</p>
      </div>
    </div>
    <div class="front-band-rule"></div>
    <p class="holder"><span class="holder-first">Marcus</span> <span class="holder-last">Oyelaran</span></p>
    <div class="divider"></div>
    <address class="contact">
      14, Jalan Cendana 5/3 Taman<br>
      Seri Cendana, 81400 Johor<br>
      Bahru, Johor, Malaysia
      <p class="contact-phone">+6011-4837-5062</p>
    </address>
  </section>

</body>
</html>
```